Ordinary Velvet Sparrow inquiring into the Mystery of her Heart needs a Book Cover design

Hello! I need a book cover design (for printed softcover 6” x 9” and eBook) for my new book titled "The Wide Season of a Modest Velvet Sparrow: Notes on Finding Room for Every Part." It's the story of a mom juggling a demanding technology career who embarks upon a self-discovery journey, faces cancer, and learns to expand her life, one vulnerable nibble at a time. With the help of a guide on her spiritual path, she learns to let go of her strong woman do-it-all persona, allowing her soul to fully shine. My purpose in writing the book is to share what I've learned about finding the "moreness" in being human.
*I would like to see book cover designs that communicate a sense of both strength and vulnerability, confidence and humbleness, curiosity and inner discovery—hinting at what's to come. I’ve uploaded a few images that I like because they feel clean and simple, and because they can be interpreted as metaphors of the beauty and power within each of us.
*If your design submission includes a mirror reflection of some sort of a “velvet sparrow” image that people are familiar with, then I would like it to convey a reluctant or questioning velvet sparrow, rather than a bold, fighting-to-save-the-world velvet sparrow.
*I lean toward a clean and calming background, as the book is really an inquiry into the mystery of this heart. It’s an examination of what I might have lost of myself, and ultimately gained, through all my crazy years of juggling. So, it’s a journey of spiritual growth.
Thank you for your interest and sharing your creative talent.

Target Market(s)

(1) Career-oriented parents, especially moms, who are in their 30's and 40's, in the midst of the struggle of trying to juggle it all; (2) life-long strivers, age 55+, who are finally slowing down and looking back to try and make sense of their lives, seeking to understand their buried inner life

Industry/Entity Type

Book Categories: Women & Business; Spiritual Self-help; Strong Women

Font styles to use
Serif

Colors

Designer to choose colors to be used in the design.

Requirements
Must have
• Clean and simple overall feeling
Nice to have
• I am open to including color—if so, perhaps some (not too much) hunter green would be nice (not required, but I’ve used it in a draft website design and rather like it).
Should not have
• Should not feel too "busy"

```html
<!DOCTYPE html>
<html lang="en">
<head>
<meta charset="utf-8">
<title>The Wide Season of a Modest Velvet Sparrow — Book Cover</title>
<link rel="stylesheet" href="https://fonts.googleapis.com/css2?family=Limelight&family=Cormorant+SC:wght@500&display=swap">
<style>
  :root {
    --coral: #e8563f;
    --cream: #f8e8b3;
    --cream-light: #fbf0c9;
    --navy: #1f2648;
    --ember: #d9472f;
  }
  html, body {
    margin: 0;
    padding: 0;
    overflow: hidden;
    background: var(--coral);
  }
  .cover {
    position: relative;
    width: 769px;
    height: 1200px;
    overflow: hidden;
    background: var(--coral);
  }
  .figure-art {
    position: absolute;
    inset: 0;
    width: 769px;
    height: 1200px;
  }
  .moon-badge {
    position: absolute;
    left: 0;
    top: 0;
    width: 260px;
    height: 250px;
  }
  .tagline {
    position: absolute;
    left: 34px;
    top: 40px;
    width: 170px;
    margin: 0;
    font-family: "Cormorant SC", serif;
    font-weight: 500;
    font-size: 23px;
    line-height: 27px;
    letter-spacing: 0.5px;
    color: var(--navy);
    text-transform: uppercase;
  }
  .title {
    position: absolute;
    left: 190px;
    top: 145px;
    width: 600px;
    margin: 0;
    font-family: "Limelight", serif;
    font-weight: 400;
    color: var(--navy);
    text-align: center;
    text-transform: uppercase;
  }
  .title span {
    display: block;
    font-size: 100px;
    line-height: 146px;
    white-space: nowrap;
  }
  .title .title-short { font-size: 92px; }
  .title .title-long { font-size: 72px; }
  .author {
    position: absolute;
    left: 0;
    top: 1030px;
    width: 740px;
    margin: 0;
    font-family: "Limelight", serif;
    font-weight: 400;
    font-size: 38px;
    line-height: 1;
    text-align: center;
    color: var(--cream);
    text-transform: uppercase;
  }
</style>
</head>
<body>
  <main class="cover">
    <svg class="figure-art" viewBox="0 0 769 1200" role="img" aria-label="Illustration area: a cream silhouette of a woman in profile with long flowing hair, rising from the lower left toward the right edge">
      <defs>
        <linearGradient id="figureTone" x1="0" y1="0" x2="0" y2="1">
          <stop offset="0" stop-color="var(--cream-light)"/>
          <stop offset="1" stop-color="var(--cream)"/>
        </linearGradient>
      </defs>
      <path d="M500 60 C640 90 745 230 750 440 C755 650 720 840 620 950 C540 990 420 975 300 990 C240 996 215 975 245 925 C320 800 350 650 370 500 C390 320 400 180 500 60 Z" fill="url(#figureTone)"/>
    </svg>

    <svg class="moon-badge" viewBox="0 0 260 250" aria-hidden="true">
      <circle cx="100" cy="100" r="118" fill="var(--cream)"/>
      <path d="M196 30 A96 96 0 0 1 196 176 A118 118 0 0 0 196 30 Z" fill="var(--ember)"/>
    </svg>
    <p class="tagline">Notes on finding room for every part</p>

    <h1 class="title">
      <span class="title-short">The</span>
      <span class="title-long">Wide Season</span>
      <span class="title-short">of a</span>
      <span>Modest</span>
      <span>Velvet</span>
      <span>Sparrow</span>
    </h1>

    <p class="author">Author Name</p>
  </main>
</body>
</html>
```